Website for UK Fintech Company specialising in Auto-Finance asset management

We need a website for a FINTECH business called KELVO Asset Management. We have developed and licenced an innovative platform to provide financial institutions whom provide secured Asset finance loans to consumer and commercial clients, allowing for real time tracking and management of defaulted accounts pending repossession. The KELVO Asset Management Platform is a total recoveries solution through the cycle, from the moment the lender has to recover the vehicle (due to default/non-payment) to the disposal of the vehicle (via sale at Motor Auctions or by selling to a Car dealership network). The data provided from external services allows the Financier to make informed decisions, such as whether it is economical to continue the recovery and decide which sales channel is better suited for their assets to maximise residual values and minimise financial losses. The KELVO platform provides an array of MI reporting and uses a systematic approach utilising exception reporting to identify key areas of non-performance to enable focus where needed. KELVO also provides a leading Debt collection service recovering end-of-cycle losses such as Financial Shortfall and losses in vehicle values due to conditions and excessive damage.

We also require a new logo for out new product called PL-Certify

Target Market(s)

Financial institutions whom provide secured Asset finance loans to consumer and commercial clients

Industry/Entity Type

Financial Service

Logo Text

PL- Certify (this is for a new product which forms part of the KELVO Asset Mangement Platform

Number of Pages Required

4 page

Font styles to use
Serif
Sans Serif

Colors

Designer to choose colors to be used in the design.

Requirements
Must have
• We need a simple website with a broken down as follows;
• • Landing page
• • Services page
• • About us page
• • KELVO Asset Management Platform login page (client facing)
Nice to have
• Our slogan is 'Auto-Finance Expertise'
• We are very much open to suggestions as long as we can create a professional/ corporate / modern feel to the website. We are a FINTECH company, and that needs to come across
Should not have
• Whilst we are an asset management company primarily managing vehicles through our platform, we don't want it to look like a car dealership website!:)

```html
<!DOCTYPE html>
<html lang="en">
<head>
<meta charset="utf-8">
<title>KELVO Asset Management – Auto-Finance Expertise</title>
<link href="https://fonts.googleapis.com/css2?family=Open+Sans:wght@400;600;700&family=Roboto+Condensed:wght@400;700&family=Hind:wght@300;400&family=Arimo:wght@400&display=swap" rel="stylesheet">
<style>
:root{
  --orange:#f07c1b;
  --orange-dark:#d9650e;
  --ink:#1c1c1c;
  --body:#6a6a6a;
  --line:#d6d6d6;
  --footer:#242424;
  --white:#ffffff;
  --pale:#f3f3f3;
}
*{box-sizing:border-box;margin:0;padding:0}
html,body{width:1200px;height:2473px;overflow:hidden;background:var(--white)}
body{position:relative;font-family:"Open Sans",sans-serif;color:var(--ink)}
.abs{position:absolute}
.center{left:0;width:1200px;text-align:center}

/* hero */
.hero{position:absolute;left:0;top:0;width:1200px;height:725px;overflow:hidden}
.hero-photo{position:absolute;inset:0;background:
  radial-gradient(ellipse at 45% 45%,#7a706a 0%,#4d4744 40%,#2a2726 75%,#1a1918 100%)}
.hero-shade{position:absolute;inset:0;background:rgba(0,0,0,.35)}
.topbar{position:absolute;left:0;top:0;width:1200px;height:41px;background:rgba(20,20,20,.55);
  font-family:"Roboto Condensed",sans-serif;font-size:13px;color:var(--white)}
.topbar-mail{position:absolute;left:160px;top:12px;display:flex;align-items:center;gap:8px}
.topbar-phone{position:absolute;right:159px;top:11px;display:flex;align-items:center;gap:7px;font-size:15px;font-weight:700}
.brand{font-family:"Open Sans",sans-serif;font-weight:700;color:var(--white)}
.nav-brand{position:absolute;left:160px;top:68px;font-size:40px;letter-spacing:-1px;line-height:1}
.menu-toggle{position:absolute;left:1014px;top:84px;width:26px;height:18px}
.menu-toggle span{display:block;height:2px;background:var(--white);margin-bottom:5px}
.hero-brand{position:absolute;left:0;top:292px;width:1200px;text-align:center}
.hero-brand .brand{font-size:84px;letter-spacing:-2px;line-height:1}
.hero-tagline{position:absolute;top:380px;font-family:"Roboto Condensed",sans-serif;font-weight:700;font-size:20px;color:var(--orange);letter-spacing:.5px}
.hero-title{position:absolute;top:446px;font-weight:600;font-size:42px;letter-spacing:7px;color:var(--white)}
.hero-arrow{position:absolute;left:585px;top:680px}

/* intro */
.intro{top:800px;left:130px;width:940px;text-align:center;font-family:"Hind",sans-serif;font-weight:300;font-size:24.5px;line-height:46px;color:#2b2b2b}
.rule{position:absolute;height:2px;width:80px;left:560px;background:var(--orange)}

/* tabs */
.tabs{position:absolute;left:277px;top:1036px;width:643px;height:31px;border-bottom:1px solid var(--line);
  display:flex;justify-content:space-between;padding:0 48px 0 49px;font-size:12.5px;font-weight:600;letter-spacing:.6px;color:#4a4a4a}
.tab{position:relative;height:30px}
.tab.active{color:var(--orange)}
.tab.active::after{content:"";position:absolute;left:50%;bottom:-4px;width:6px;height:6px;margin-left:-3px;border-radius:50%;background:var(--orange)}
.service-text{top:1115px;left:325px;width:550px;text-align:center;font-family:"Arimo",sans-serif;font-size:12.5px;line-height:27px;color:var(--body)}
.btn{position:absolute;display:flex;align-items:center;justify-content:center;font-size:10.5px;font-weight:700;letter-spacing:.5px;border:1.5px solid #333;color:var(--ink);background:var(--white)}

/* platform band */
.platform{position:absolute;left:0;top:1417px;width:1200px;height:503px;background:var(--pale);overflow:hidden}
.platform-backdrop{position:absolute;inset:0;background:
  linear-gradient(120deg,#ec7a1c 0%,#f29a4c 18%,#f3f3f3 38%,#f3f3f3 66%,#f29a4c 84%,#ec7a1c 100%)}
.platform-title{position:absolute;top:81px;font-weight:700;font-size:28px;letter-spacing:3px;color:var(--ink)}
.platform-text{position:absolute;left:295px;top:168px;width:610px;text-align:center;font-family:"Arimo",sans-serif;font-size:12.5px;line-height:28px;color:var(--body)}
.dashed{position:absolute;left:313px;top:254px;width:569px;border-top:1px dashed #bdbdbd}
.product-label{position:absolute;top:290px;font-size:13px;font-weight:700;letter-spacing:1.5px;color:var(--ink)}
.product-name{position:absolute;top:340px;font-weight:700;font-size:46px;color:var(--orange-dark)}

/* subscribe */
.email-field{position:absolute;left:384px;top:1990px;width:432px;height:32px;border-bottom:1px solid #c9c9c9;font-size:11.5px;color:#9a9a9a;padding-left:10px;padding-top:4px}

/* footer */
.footer{position:absolute;left:0;top:2139px;width:1200px;height:334px;background:var(--footer);color:var(--white)}
.footer .btn{background:transparent;border-color:#d6d6d6;color:var(--white)}
.footer-brand{position:absolute;left:0;top:50px;width:1200px;text-align:center}
.footer-brand .brand{font-size:48px;letter-spacing:-1px;line-height:1}
.footer-tagline{position:absolute;top:107px;font-family:"Roboto Condensed",sans-serif;font-weight:700;font-size:12px;color:var(--orange)}
.footer-line{position:absolute;font-size:11.5px;color:var(--white)}
.footer-line a{color:var(--orange);text-decoration:none}
.social{position:absolute;left:531px;top:284px;display:flex;gap:32px}
.social span{width:12px;height:12px;border-radius:50%;background:#8a8a8a}
</style>
</head>
<body>

<header class="hero">
  <div class="hero-photo" role="img" aria-label="Photograph of a businessman in a car reviewing finance paperwork with an advisor"></div>
  <div class="hero-shade"></div>

  <div class="topbar">
    <div class="topbar-mail">
      <svg width="14" height="10" viewBox="0 0 14 10"><rect x=".75" y=".75" width="12.5" height="8.5" fill="none" stroke="#fff" stroke-width="1.5"/><path d="M1 1l6 5 6-5" fill="none" stroke="#fff" stroke-width="1.5"/></svg>
      info@kelvoassetplatform.com
    </div>
    <div class="topbar-phone">
      <svg width="12" height="14" viewBox="0 0 12 14"><path d="M3 0l2 3.5-1.5 1.5c.8 2 2 3.5 4 4.5L9 8l3 2-1 3c-5 0-11-6-11-11z" fill="#fff"/></svg>
      020 7946 0381
    </div>
  </div>

  <div class="nav-brand brand">KELVO</div>
  <div class="menu-toggle"><span></span><span></span><span></span></div>

  <div class="hero-brand"><span class="brand">KELVO</span></div>
  <div class="hero-tagline abs center">ASSET MANAGEMENT PLATFORM</div>
  <h1 class="hero-title center">AUTO-FINANCE EXPERTISE</h1>
  <svg class="hero-arrow" width="30" height="16" viewBox="0 0 30 16"><path d="M2 2l13 12L28 2" fill="none" stroke="#fff" stroke-width="2"/></svg>
</header>

<p class="intro abs">Lorem ipsum dolor sit amet, consectetur adipiscing elit, sed do eiusmod tempor incididunt ut labore et dolore magna aliqua. Ut enim ad minim veniam, quis nostrud exercitation ullamco laboris nisi ut aliquip ex ea commodo consequat.</p>
<div class="rule" style="top:976px"></div>

<nav class="tabs">
  <span class="tab active">AUTO-FINANCE</span>
  <span class="tab">ASSET MANAGEMENT</span>
  <span class="tab">ASSET FINANCE LOANS</span>
</nav>
<p class="service-text abs">Lorem ipsum dolor sit amet, consectetur adipiscing elit, sed do eiusmod tempor incididunt ut labore et dolore magna aliqua. Ut enim ad minim veniam, quis nostrud exercitation ullamco laboris nisi ut aliquip ex ea commodo consequat. Duis aute irure dolor in reprehenderit in voluptate velit esse cillum dolore eu fugiat nulla pariatur. Excepteur sint occaecat cupidatat non proident, sunt in culpa qui officia deserunt mollit anim id est laborum.</p>
<div class="btn" style="left:511px;top:1294px;width:176px;height:35px">MORE ABOUT SERVICE</div>

<section class="platform">
  <div class="platform-backdrop" role="img" aria-label="Abstract orange background artwork framing the section"></div>
  <h2 class="platform-title center">KELVO ASSET MANAGEMENT</h2>
  <div class="rule" style="top:130px"></div>
  <p class="platform-text">Lorem ipsum dolor sit amet, consectetur adipiscing elit, sed do eiusmod tempor incididunt ut labore et dolore magna aliqua. Ut enim ad minim veniam, quis nostrud exercitation ullamco laboris</p>
  <div class="dashed"></div>
  <div class="product-label center">OUR NEW PRODUCT</div>
  <div class="product-name center">PL-Certify</div>
</section>

<div class="email-field">Enter Your Email Here</div>
<div class="btn" style="left:531px;top:2047px;width:137px;height:36px">SUBSCRIBE</div>

<footer class="footer">
  <div class="btn" style="left:257px;top:63px;width:178px;height:35px">CONTACT US</div>
  <div class="btn" style="left:765px;top:63px;width:178px;height:35px">ASSET FINANCE LOANS</div>
  <div class="footer-brand"><span class="brand">KELVO</span></div>
  <div class="footer-tagline center">ASSET MANAGEMENT PLATFORM</div>
  <div class="footer-line center" style="top:166px">1508 Lorem Ipsum Dolor Sit Amet Consectetur</div>
  <div class="footer-line center" style="top:193px">020.7946.0382 &nbsp;/&nbsp; <a href="#">info@kelvoassetplatform.com</a></div>
  <div class="footer-line center" style="top:239px">© Copyright 2018 KELVO Asset Management Platform.</div>
  <div class="social" aria-label="Social links"><span></span><span></span><span></span><span></span></div>
</footer>

</body>
</html>
```